Harbour Thread Studio business card design

I need to get some business cards printed ready for company launch but my own designs look a bit basic and not very exciting, I hope you can help with something more eye catching.

I will be giving these to business owners, event organisers, brand managers etc. in a professional capacity with the aim that they keep me in mind and get in contact when they need to order embroidered/printed clothing items in future.
This is a basic website whilst new one is developed but the about us tab will give you better insight to the work i am looking for.

I also have facebook and instagram links on website so maybe if space for those icons?
also a business whatsapp account which there is a QR code for and something i may wish to include on the reverse so it's really easy for people to start a conversation.

Target Market(s)

Business to business

Industry/Entity Type

textile embroidery and printing

Contact Information for Business Card

name, job title, web address, email address

Font styles to use
Sans Serif
Other font styles liked:
• Monseratt is in the logo

Requirements
Must have
• name, job title, web address, email address, logo - nice design
Nice to have
• whatsapp qr link, social logos
Should not have
• no need for business address

```html
<!DOCTYPE html>
<html lang="en">
<head>
<meta charset="utf-8">
<title>Harbour Thread Studio – Business Card</title>
<link href="https://fonts.googleapis.com/css2?family=Montserrat:wght@500;600;700&display=swap" rel="stylesheet">
<style>
  :root {
    --brand-blue: #5b7be6;
    --text-blue: #5575dc;
    --coral: #f5a191;
    --wave-blue: #d2dcf8;
    --ring-grey: #6e8284;
    --paper: #ffffff;
  }
  html, body {
    margin: 0;
    padding: 0;
    width: 1200px;
    height: 1200px;
    overflow: hidden;
    background: var(--brand-blue);
  }
  .card {
    position: relative;
    width: 1200px;
    height: 1200px;
    background: var(--brand-blue);
    font-family: "Montserrat", sans-serif;
  }
  .card__panel {
    position: absolute;
    inset: 39px;
    background: var(--paper);
    overflow: hidden;
  }
  .card__waves {
    position: absolute;
    left: 0;
    top: 0;
    width: 1122px;
    height: 1122px;
  }
  .card__stitch {
    position: absolute;
    inset: 69px;
    border: 2px dashed var(--brand-blue);
    pointer-events: none;
  }
  .logo {
    position: absolute;
    left: 463px;
    top: 160px;
    width: 274px;
    height: 274px;
    box-sizing: border-box;
    border: 7px solid var(--ring-grey);
    border-radius: 50%;
    display: flex;
    align-items: center;
    justify-content: center;
    text-align: center;
  }
  .logo__name {
    margin: 0;
    font-weight: 700;
    font-size: 30px;
    line-height: 1.2;
    letter-spacing: 2px;
    color: var(--text-blue);
    text-transform: uppercase;
  }
  .person {
    position: absolute;
    left: 0;
    right: 0;
    top: 455px;
    text-align: center;
  }
  .person__name {
    margin: 0;
    font-weight: 700;
    font-size: 69px;
    letter-spacing: 1.5px;
    color: var(--text-blue);
    line-height: 1;
  }
  .person__role {
    margin: 30px auto 0;
    display: flex;
    align-items: center;
    justify-content: center;
    gap: 26px;
    font-weight: 600;
    font-size: 50px;
    color: var(--coral);
    line-height: 1;
  }
  .person__rule {
    width: 183px;
    height: 4px;
    background: var(--coral);
  }
  .contacts {
    position: absolute;
    left: 130px;
    top: 645px;
    margin: 0;
    padding: 0;
    list-style: none;
  }
  .contacts__item {
    display: flex;
    align-items: center;
    height: 56px;
    margin-bottom: 22px;
    font-weight: 500;
    font-size: 41px;
    color: var(--text-blue);
  }
  .contacts__icons {
    width: 140px;
    display: flex;
    justify-content: flex-end;
    padding-right: 14px;
    box-sizing: border-box;
  }
  .contacts__icons svg { display: block; }
  .social-dot {
    width: 56px;
    height: 56px;
    border-radius: 50%;
    background: var(--brand-blue);
  }
  .website {
    position: absolute;
    left: 0;
    right: 0;
    top: 1037px;
    margin: 0;
    text-align: center;
    font-weight: 700;
    font-size: 42px;
    letter-spacing: 1px;
    color: var(--text-blue);
  }
</style>
</head>
<body>
  <main class="card">
    <div class="card__panel">
      <svg class="card__waves" viewBox="0 0 1122 1122" aria-hidden="true">
        <path d="M0 872 C 140 852, 280 892, 420 872 S 700 852, 840 872 S 1060 892, 1122 872"
              fill="none" stroke="var(--wave-blue)" stroke-width="16"/>
        <path d="M0 912 C 140 892, 280 932, 420 912 S 700 892, 840 912 S 1060 932, 1122 912"
              fill="none" stroke="var(--wave-blue)" stroke-width="16"/>
        <path d="M0 958 C 140 938, 280 978, 420 958 S 700 938, 840 958 S 1060 978, 1122 958 L1122 1122 L0 1122 Z"
              fill="var(--wave-blue)"/>
      </svg>
    </div>
    <div class="card__stitch"></div>

    <div class="logo">
      <p class="logo__name">Harbour<br>Thread<br>Studio</p>
    </div>

    <header class="person">
      <h1 class="person__name">ROWAN ASHBY</h1>
      <div class="person__role">
        <span class="person__rule"></span>
        <span>Director</span>
        <span class="person__rule"></span>
      </div>
    </header>

    <ul class="contacts">
      <li class="contacts__item">
        <span class="contacts__icons">
          <svg width="56" height="56" viewBox="0 0 56 56" aria-label="Phone">
            <circle cx="28" cy="28" r="28" fill="var(--brand-blue)"/>
            <rect x="19" y="11" width="18" height="34" rx="3.5" fill="none" stroke="#fff" stroke-width="3"/>
            <line x1="25" y1="40" x2="31" y2="40" stroke="#fff" stroke-width="2.5" stroke-linecap="round"/>
          </svg>
        </span>
        <span>078 5120 4471</span>
      </li>
      <li class="contacts__item">
        <span class="contacts__icons">
          <svg width="56" height="56" viewBox="0 0 56 56" aria-label="Email">
            <circle cx="28" cy="28" r="28" fill="var(--brand-blue)"/>
            <rect x="13" y="17" width="30" height="22" rx="2.5" fill="none" stroke="#fff" stroke-width="3"/>
            <path d="M14 19 L28 30 L42 19" fill="none" stroke="#fff" stroke-width="3" stroke-linejoin="round"/>
          </svg>
        </span>
        <span>rowan@harbourthreadstudio.com</span>
      </li>
      <li class="contacts__item">
        <span class="contacts__icons">
          <span class="social-dot" aria-hidden="true"></span>
        </span>
        <span>@harbour thread studio</span>
      </li>
    </ul>

    <p class="website">WWW.HARBOURTHREADSTUDIO.COM</p>
  </main>
</body>
</html>
```